Newsletter-Design für Print - tornhof partner
Zielgruppe
tornhof partner business hat sich auf die Kaltakquise und den Vertrieb spezialisiert. Generell agieren wir ausschließlich im BtoB Bereich überwiegend für die Industrie.
Aufgabenstellung
verwenden unserer Logofarben - Blau und Rot - maximal noch grau - sehr puristisch und minimalistisch - klare Struktur für case studiens - checklisten - whitepapers

```html
<!DOCTYPE html>
<html lang="de">
<head>
<meta charset="utf-8">
<title>Newsletter – tornhof partner</title>
<link rel="stylesheet" href="https://fonts.googleapis.com/css2?family=Exo+2:wght@300;400;500;600;700&display=swap">
<style>
  :root {
    --red: #c8191a;
    --red-dark: #a01414;
    --blue: #0d4a8a;
    --grey-head: #868686;
    --grey-text: #8a8a8a;
    --ink: #141414;
    --white: #ffffff;
    --lh: 19.9px;
  }
  * { margin: 0; padding: 0; box-sizing: border-box; }
  html, body { width: 848px; height: 1200px; overflow: hidden; background: var(--white); }
  body { font-family: "Exo 2", Arial, sans-serif; }
  .page { position: relative; width: 848px; height: 1200px; overflow: hidden; background: var(--white); }

  .masthead {
    position: absolute; left: 0; top: 0; width: 848px; height: 343px;
    background: linear-gradient(180deg, var(--red) 0%, #c01818 60%, var(--red-dark) 100%);
  }
  .issue {
    position: absolute; left: 24px; top: 12px;
    color: var(--white); font-size: 25px; font-weight: 500; letter-spacing: 0.2px;
  }
  .title {
    position: absolute; left: 0; top: 206px; width: 848px;
    color: var(--white); font-size: 121px; font-weight: 700; line-height: 1;
    letter-spacing: -2px; text-align: center; white-space: nowrap;
  }

  .headline {
    position: absolute; left: 38px; top: 395px;
    color: var(--grey-head); font-size: 42.5px; font-weight: 700; line-height: 48px;
    white-space: nowrap;
  }

  .body-text {
    position: absolute; color: var(--grey-text);
    font-size: 13.3px; font-weight: 300; line-height: var(--lh);
    letter-spacing: -0.1px;
  }
  .ln {
    display: block; height: var(--lh); white-space: nowrap;
    text-align: justify; text-align-last: justify;
  }
  .ln.end { text-align-last: left; }
  .ln.gap { height: var(--lh); }

  .quote {
    position: absolute; left: 172px; top: 679px;
    color: var(--ink); font-size: 26.5px; font-weight: 400; line-height: 31.3px;
    white-space: nowrap;
  }

  .teaser { position: absolute; left: 606px; width: 202px; }
  .teaser-title {
    color: var(--blue); font-size: 25px; font-weight: 700; line-height: 31px;
  }
  .teaser-text {
    margin-top: 4px; color: var(--grey-text);
    font-size: 13.2px; font-weight: 300; line-height: 20px; text-align: justify;
  }
  .teaser-page {
    display: block; text-align: right; color: var(--blue);
    font-size: 13.5px; font-weight: 500; line-height: 20px;
  }
  .divider {
    position: absolute; height: 0; border-top: 2.5px dotted var(--ink);
  }

  .brand {
    position: absolute; left: 0; top: 1118px; width: 848px; text-align: center;
    color: var(--blue); font-size: 40px; font-weight: 500; line-height: 52px; letter-spacing: 0.5px;
  }
  .footer-band {
    position: absolute; left: 0; bottom: 0; width: 848px; height: 21px; background: var(--red);
  }
</style>
</head>
<body>
<div class="page">
  <header class="masthead">
    <div class="issue">No 01 / Oktober 2017</div>
    <div class="title">NEWSLETTER</div>
  </header>

  <h1 class="headline">Hier Platz für eine<br>Headline lorem ipsum est</h1>

  <!-- column 1 -->
  <div class="body-text" style="left:40px; top:508px; width:261px;">
    <span class="ln">Lorem ipsum dolor sit amet, consectetu-</span>
    <span class="ln">er adipiscing elit. Aenean commodo ligula</span>
    <span class="ln">eget dolor. Aenean massa. Cum sociis na-</span>
    <span class="ln">toque penatibus et magnis dis parturient</span>
    <span class="ln">montes, nascetur ridiculus mus. Donec</span>
    <span class="ln">quam felis, ultricies nec, pellentesque eu,</span>
    <span class="ln">pretium quis, sem. Nulla consequat mas-</span>
  </div>
  <div class="body-text" style="left:40px; top:647.3px; width:107px;">
    <span class="ln">sa quis enim.</span>
    <span class="ln">Donec pede</span>
    <span class="ln">justo, fringilla</span>
    <span class="ln">vel, aliquet nec,</span>
    <span class="ln">vulputate eget,</span>
    <span class="ln">arcu. In enim</span>
    <span class="ln">justo, rhoncus</span>
    <span class="ln">ut, imperdiet a,</span>
    <span class="ln">venenatis vitae,</span>
    <span class="ln">justo. Nullam</span>
    <span class="ln">dictum felis eu</span>
  </div>
  <div class="body-text" style="left:40px; top:866.2px; width:261px;">
    <span class="ln">pede mollis pretium. Integer tincidunt.</span>
    <span class="ln">Cras dapibus. Vivamus elementum sem-</span>
    <span class="ln">per nisi. Aenean vulputate eleifend tellus.</span>
    <span class="ln">Aenean leo ligula, porttitor eu, consequat</span>
    <span class="ln end">vitae, eleifend ac, enim.</span>
    <span class="ln gap"></span>
    <span class="ln">Aliquam lorem ante, dapibus in, viverra</span>
    <span class="ln">quis, feugiat a, tellus. Phasellus viverra</span>
    <span class="ln">nulla ut metus varius laoreet. Quisque</span>
    <span class="ln">rutrum. Aenean imperdiet. Etiam ultricies</span>
  </div>

  <!-- column 2 -->
  <div class="body-text" style="left:321px; top:508px; width:260px;">
    <span class="ln">nisi vel augue. Curabitur ullamcorper ul-</span>
    <span class="ln">tricies nisi. Nam eget dui. Etiam rhoncus.</span>
    <span class="ln">Maecenas tempus, tellus eget condimen-</span>
    <span class="ln">tum rhoncus, sem quam semper libero,</span>
    <span class="ln">sit amet adipiscing sem neque sed ipsum.</span>
    <span class="ln">Nam quam nunc, blandit vel, luctus pul-</span>
    <span class="ln">vinar, hendrerit id, lorem. Maecenas nec</span>
  </div>
  <div class="body-text" style="left:489px; top:647.3px; width:92px;">
    <span class="ln">odio et ante</span>
    <span class="ln">tincidunt tem-</span>
    <span class="ln">pus. Donec</span>
    <span class="ln">vitae sapien</span>
    <span class="ln">ut libero vene-</span>
    <span class="ln">natis faucibus.</span>
    <span class="ln">Nullam quis</span>
    <span class="ln">ante. Etiam sit</span>
    <span class="ln">amet orci eget</span>
    <span class="ln">eros faucibus</span>
    <span class="ln">tincidunt. Duis</span>
  </div>
  <div class="body-text" style="left:321px; top:866.2px; width:260px;">
    <span class="ln">leo. Sed fringilla mauris sit amet nibh.</span>
    <span class="ln end">Donec sodales sagittis magna.</span>
    <span class="ln gap"></span>
    <span class="ln">Sed consequat, leo eget bibendum so-</span>
    <span class="ln">dales, augue velit cursus nunc, Lorem</span>
    <span class="ln">ipsum dolor sit amet, consectetuer adi-</span>
    <span class="ln">piscing elit. Aenean commodo ligula eget</span>
    <span class="ln">dolor. Aenean massa. Cum sociis natoque</span>
    <span class="ln">penatibus et magnis dis parturient mon-</span>
    <span class="ln">tes, nascetur sodales, augue velit cursus</span>
  </div>

  <blockquote class="quote">„Zitat aus dem Artikel<br>dolor sit amet, consec-<br>tetuer adipiscing elit.<br>Aenean commodo ligu-<br>la eget dolor est.</blockquote>

  <!-- sidebar teasers -->
  <article class="teaser" style="top:510px;">
    <h2 class="teaser-title">Thema 01<br>Headline lorem</h2>
    <p class="teaser-text">Lorem ipsum dolor sit amet, consectetuer adipiscing elit. Aenean commodo ligula eget dolor. Aenean massa</p>
    <span class="teaser-page">Seite 02</span>
  </article>
  <div class="divider" style="left:606px; top:687px; width:202px;"></div>

  <article class="teaser" style="top:712px;">
    <h2 class="teaser-title">Thema 02<br>Headline lorem</h2>
    <p class="teaser-text">Lorem ipsum dolor sit amet, consectetuer adipiscing elit. Aenean commodo ligula eget dolor. Aenean massa</p>
    <span class="teaser-page">Seite 04</span>
  </article>
  <div class="divider" style="left:606px; top:887px; width:202px;"></div>

  <article class="teaser" style="top:914px;">
    <h2 class="teaser-title">Thema 03<br>Headline lorem</h2>
    <p class="teaser-text">Lorem ipsum dolor sit amet, consectetuer adipiscing elit. Aenean commodo ligula eget dolor. Aenean massa</p>
    <span class="teaser-page">Seite 06</span>
  </article>

  <div class="divider" style="left:40px; top:1107px; width:773px;"></div>

  <div class="brand">tornhof partner</div>
  <div class="footer-band"></div>
</div>
</body>
</html>
```